Law Offices business card

Hi there, I'll need business card for the Law Offices of Colby Marchetti. The information must convey his strategic approach and quick resolution to complex business litigation needs. Please emphasize Civil Litigation, Corporate Law, Business Governance and Real Estate Law. Colby has over 25 years of experience in these fields.The card should be modern and edgy and the message should be clear. Please consult his current website for ideas.

```html
<!DOCTYPE html>
<html lang="en">
<head>
<meta charset="utf-8">
<title>Law Offices of Colby Marchetti — Business Card</title>
<link rel="stylesheet" href="https://fonts.googleapis.com/css2?family=Cinzel:wght@400;600&family=Open+Sans:wght@400;600;700&display=swap">
<style>
  :root {
    --stage: #e9e6e1;
    --ink: #111111;
    --paper: #ffffff;
    --accent: #e8731f;
    --muted: #333333;
    --serif: "Cinzel", "Times New Roman", serif;
    --sans: "Open Sans", Arial, sans-serif;
  }
  * { box-sizing: border-box; margin: 0; padding: 0; }
  html, body { width: 1200px; height: 900px; overflow: hidden; }
  body { background: var(--stage); position: relative; font-family: var(--sans); }

  .card {
    position: absolute;
    width: 640px;
    height: 366px;
    border-radius: 4px;
    overflow: hidden;
    box-shadow: 0 6px 18px rgba(0,0,0,0.18);
  }

  /* Back of card */
  .card--back {
    left: 500px; top: 50px;
    background: var(--ink);
    color: var(--paper);
  }
  .card--back .firm-name {
    position: absolute;
    left: 0; right: 0; top: 88px;
    text-align: center;
    font-family: var(--serif);
    font-weight: 400;
    line-height: 1.05;
  }
  .card--back .firm-name__top { display: block; font-size: 54px; letter-spacing: 3px; }
  .card--back .firm-name__bottom { display: block; font-size: 36px; letter-spacing: 2px; }
  .card--back .practice-areas {
    position: absolute;
    left: 20px; right: 20px; top: 238px;
    text-align: center;
    font-size: 14px;
    font-weight: 600;
    line-height: 22px;
  }
  .practice-areas__years { display: block; color: var(--accent); }

  /* Front of card */
  .card--front {
    left: 60px; top: 470px;
    background: var(--paper);
    color: var(--ink);
  }
  .card__shapes { position: absolute; inset: 0; }
  .holder {
    position: absolute;
    left: 70px; top: 20px;
  }
  .holder__name { color: var(--accent); font-weight: 700; font-size: 20px; line-height: 1.15; }
  .holder__title { font-size: 12px; color: var(--muted); }

  .contact {
    position: absolute;
    left: 48px; top: 112px;
    font-size: 14px;
    line-height: 19px;
    color: var(--ink);
    list-style: none;
  }
  .contact__address { margin-left: 22px; margin-bottom: 4px; }
  .contact__item { display: flex; align-items: center; gap: 10px; }
  .contact__icon { width: 12px; height: 12px; flex: none; }

  .firm-mark {
    position: absolute;
    left: 340px; top: 104px;
    width: 290px;
    text-align: center;
  }
  .firm-mark__dot {
    width: 74px; height: 74px;
    border-radius: 50%;
    background: var(--ink);
    margin: 0 auto 12px;
  }
  .firm-mark__name {
    font-family: var(--serif);
    font-weight: 400;
    color: var(--ink);
    font-size: 20px;
    line-height: 1.2;
    letter-spacing: 0.5px;
    white-space: nowrap;
  }
</style>
</head>
<body>

  <section class="card card--back" aria-label="Card back">
    <h1 class="firm-name">
      <span class="firm-name__top">Law Offices</span>
      <span class="firm-name__bottom">Of Colby Marchetti</span>
    </h1>
    <p class="practice-areas">
      Civil Litigation - Corporate Law - Business Governance - Real Estate Law
      <span class="practice-areas__years">Over 25 Years of Experience</span>
    </p>
  </section>

  <section class="card card--front" aria-label="Card front">
    <svg class="card__shapes" width="640" height="366" viewBox="0 0 640 366" aria-hidden="true">
      <polygon points="0,0 60,0 60,8 34,8 16,36 0,36" fill="var(--accent)"/>
      <polygon points="36,12 60,12 60,36 20,36" fill="var(--ink)"/>
      <polygon points="0,262 300,262 290,284 0,284" fill="var(--accent)"/>
      <polygon points="300,318 640,318 640,366 270,366 270,348" fill="var(--ink)"/>
      <polygon points="270,346 298,318 304,318 276,346" fill="var(--paper)"/>
    </svg>

    <div class="holder">
      <p class="holder__name">Colby Marchetti</p>
      <p class="holder__title">Attorney</p>
    </div>

    <ul class="contact">
      <li class="contact__address">118B Harbor Lane<br>Palm Cove, Florida 33410</li>
      <li class="contact__item">
        <svg class="contact__icon" viewBox="0 0 12 12" aria-hidden="true"><path d="M2 1h3l1 3-1.5 1a6 6 0 0 0 2.5 2.5L8 6l3 1v3c0 .6-.4 1-1 1A9 9 0 0 1 1 2c0-.6.4-1 1-1z" fill="var(--accent)"/></svg>
        555-210-4836
      </li>
      <li class="contact__item">
        <svg class="contact__icon" viewBox="0 0 12 12" aria-hidden="true"><rect x="1" y="4" width="10" height="7" rx="1" fill="var(--accent)"/><rect x="3" y="1" width="6" height="4" fill="var(--accent)"/></svg>
        555-210-4937
      </li>
      <li class="contact__item">
        <svg class="contact__icon" viewBox="0 0 12 12" aria-hidden="true"><rect x="0.5" y="2" width="11" height="8" fill="var(--accent)"/><path d="M1 2.5l5 4 5-4" stroke="var(--paper)" stroke-width="1" fill="none"/></svg>
        colby@marchettilaw.com
      </li>
      <li class="contact__item">
        <svg class="contact__icon" viewBox="0 0 12 12" aria-hidden="true"><circle cx="6" cy="6" r="5.5" fill="var(--accent)"/></svg>
        www.marchettilaw.com
      </li>
    </ul>

    <div class="firm-mark">
      <div class="firm-mark__dot" aria-hidden="true"></div>
      <p class="firm-mark__name">Law Offices<br>Of Colby Marchetti</p>
    </div>
  </section>

</body>
</html>
```